Sundeck construction company in need of creative business cards

We provide all round services for a variety of different deck types. Our core 3 things are vinyl decking, aluminum railings and wood decks. We want to use 3 different solid 15 gauge plastic cards with one side having a picture of either a railing, vinyl deck or a wood deck (then depending on what the client wants we can give them the card that best suites there needs) we would also want our logo layered overtop of the picture. On the other side we would have our logo and info
Updates

Sorry was busy in meetings all day will be reviewing now

1 I had posted wrong picture for railings please revise
2 Address is 2243-10562 Bramblefield Road
                    Richmond B.C.
V6K 3M2

We like the front design of #1566013

Target Market(s)

Single family residential

Industry/Entity Type

Construction

Requirements
Must have
• 3 different pictures on back of card for vinyl deckin, aluminum railings and wood decks

```html
<!DOCTYPE html>
<html lang="en">
<head>
<meta charset="utf-8">
<title>Cedarline Sundecks Business Cards</title>
<link rel="stylesheet" href="https://fonts.googleapis.com/css2?family=Arimo:wght@400;700&display=swap">
<style>
  :root {
    --page-bg: #e6e7e9;
    --card-white: #ffffff;
    --brand-green: #2f8a2f;
    --brand-green-light: #62b531;
    --brand-navy: #25315e;
    --text-white: #ffffff;
    --shadow: rgba(0,0,0,0.18);
  }
  * { margin: 0; padding: 0; box-sizing: border-box; }
  html, body { width: 1200px; height: 861px; overflow: hidden; }
  body {
    background: var(--page-bg);
    font-family: "Arimo", Arial, sans-serif;
    position: relative;
  }
  .card {
    position: absolute;
    width: 500px;
    height: 286px;
    background: var(--card-white);
    overflow: hidden;
    box-shadow: 0 6px 18px var(--shadow);
  }
  .card--railing { left: 70px;  top: 110px; }
  .card--wood    { left: 630px; top: 110px; }
  .card--vinyl   { left: 70px;  top: 450px; }
  .card--info    { left: 630px; top: 450px; }

  .photo {
    position: absolute;
    top: 0; right: 0;
    width: 80%;
    height: 100%;
  }
  .photo--railing { background: linear-gradient(160deg, #9fb3c7 0%, #7e9a86 40%, #5d7a55 65%, #4c4f55 100%); }
  .photo--wood    { background: linear-gradient(165deg, #6f7a5a 0%, #b08a62 45%, #9c6c44 75%, #7a5232 100%); }
  .photo--vinyl   { background: linear-gradient(160deg, #8e8f94 0%, #a3a09c 45%, #8c8a86 75%, #6f7c5c 100%); }
  .photo-fade {
    position: absolute;
    inset: 0;
    background: linear-gradient(90deg, #ffffff 0%, rgba(255,255,255,0.95) 22%, rgba(255,255,255,0.4) 48%, rgba(255,255,255,0) 70%),
                linear-gradient(0deg, rgba(255,255,255,0.85) 0%, rgba(255,255,255,0) 35%);
  }

  .brand {
    position: absolute;
    display: flex;
    align-items: center;
    gap: 8px;
  }
  .brand-dot {
    width: 22px; height: 22px;
    border-radius: 50%;
    background: var(--brand-green);
    flex: none;
  }
  .brand-name {
    font-family: "Arimo", Arial, sans-serif;
    font-weight: 700;
    font-size: 17px;
    letter-spacing: 0.5px;
    color: var(--brand-green);
    text-transform: uppercase;
    white-space: nowrap;
  }
  .card--railing .brand,
  .card--wood .brand,
  .card--vinyl .brand { left: 48px; top: 236px; }

  .card--info .brand { left: 12px; top: 146px; gap: 6px; }
  .card--info .brand-dot { width: 16px; height: 16px; }
  .card--info .brand-name { font-size: 15px; letter-spacing: 0; }

  .info-art { position: absolute; inset: 0; }

  .contact {
    position: absolute;
    left: 300px;
    top: 54px;
    color: var(--text-white);
  }
  .contact-name {
    font-size: 19px;
    font-weight: 700;
    margin-bottom: 14px;
  }
  .contact-list { list-style: none; }
  .contact-item {
    display: flex;
    align-items: flex-start;
    gap: 7px;
    font-size: 10.5px;
    line-height: 13px;
    margin-bottom: 7px;
  }
  .contact-icon {
    width: 13px; height: 13px;
    flex: none;
  }
</style>
</head>
<body>

  <section class="card card--railing">
    <div class="photo photo--railing" role="img" aria-label="Glass-panel aluminum railing on a balcony overlooking a city waterfront"></div>
    <div class="photo-fade"></div>
    <div class="brand"><span class="brand-dot"></span><span class="brand-name">Cedarline Sundecks</span></div>
  </section>

  <section class="card card--wood">
    <div class="photo photo--wood" role="img" aria-label="Sunlit wood deck with wicker chairs and a metal railing"></div>
    <div class="photo-fade"></div>
    <div class="brand"><span class="brand-dot"></span><span class="brand-name">Cedarline Sundecks</span></div>
  </section>

  <section class="card card--vinyl">
    <div class="photo photo--vinyl" role="img" aria-label="Speckled grey vinyl deck surface with a bench and potted plants"></div>
    <div class="photo-fade"></div>
    <div class="brand"><span class="brand-dot"></span><span class="brand-name">Cedarline Sundecks</span></div>
  </section>

  <section class="card card--info">
    <svg class="info-art" viewBox="0 0 500 286" width="500" height="286" aria-hidden="true">
      <defs>
        <linearGradient id="panelGreen" x1="0" y1="0" x2="1" y2="1">
          <stop offset="0" stop-color="#62b531"/>
          <stop offset="1" stop-color="#1f7a2e"/>
        </linearGradient>
      </defs>
      <g transform="translate(14 0)">
        <path d="M290 0 C252 90 262 210 318 286 L500 286 L500 0 Z" fill="url(#panelGreen)"/>
        <path d="M278 0 C240 90 250 210 306 286 L300 286 C238 210 228 95 262 0 Z" fill="#2f8a2f"/>
        <path d="M252 14 C214 105 228 215 290 286 L282 286 C212 218 198 110 246 14 Z" fill="#25315e"/>
      </g>
    </svg>

    <div class="brand"><span class="brand-dot"></span><span class="brand-name">Cedarline Sundecks</span></div>

    <div class="contact">
      <p class="contact-name">Dean Whitcombe</p>
      <ul class="contact-list">
        <li class="contact-item">
          <svg class="contact-icon" viewBox="0 0 14 14"><circle cx="7" cy="7" r="7" fill="#25315e"/><path d="M7 3a2.4 2.4 0 0 0-2.4 2.4C4.6 7.3 7 10.8 7 10.8s2.4-3.5 2.4-5.4A2.4 2.4 0 0 0 7 3z" fill="#fff"/><circle cx="7" cy="5.4" r="0.9" fill="#25315e"/></svg>
          <span>2243-10562 Bramblefield Road<br>Richmond B.C. V6K 3M2</span>
        </li>
        <li class="contact-item">
          <svg class="contact-icon" viewBox="0 0 14 14"><circle cx="7" cy="7" r="7" fill="#25315e"/><path d="M4.3 3.6l1.5-.4 1 2-1 .8a5 5 0 0 0 2.2 2.2l.8-1 2 1-.4 1.5c-3.3.2-6.3-2.8-6.1-6.1z" fill="#fff"/></svg>
          <span>604-555-0147</span>
        </li>
        <li class="contact-item">
          <svg class="contact-icon" viewBox="0 0 14 14"><circle cx="7" cy="7" r="7" fill="#25315e"/><rect x="4.8" y="3" width="4.4" height="8" rx="0.8" fill="#fff"/><rect x="5.5" y="4" width="3" height="5" fill="#25315e"/></svg>
          <span>604-555-0182</span>
        </li>
        <li class="contact-item">
          <svg class="contact-icon" viewBox="0 0 14 14"><circle cx="7" cy="7" r="7" fill="#25315e"/><rect x="4.5" y="3.2" width="5" height="3" fill="#fff"/><rect x="3.4" y="6.2" width="7.2" height="4.2" rx="0.6" fill="#fff"/></svg>
          <span>604-555-0163</span>
        </li>
        <li class="contact-item">
          <svg class="contact-icon" viewBox="0 0 14 14"><circle cx="7" cy="7" r="7" fill="#25315e"/><rect x="3.5" y="4.5" width="7" height="5" fill="#fff"/><path d="M3.5 4.5L7 7.3l3.5-2.8" fill="none" stroke="#25315e" stroke-width="0.8"/></svg>
          <span>dean@cedarlinevinyl.com</span>
        </li>
        <li class="contact-item">
          <svg class="contact-icon" viewBox="0 0 14 14"><circle cx="7" cy="7" r="7" fill="#25315e"/><circle cx="7" cy="7" r="3.6" fill="none" stroke="#fff" stroke-width="0.9"/><path d="M3.4 7h7.2M7 3.4c-1.6 2-1.6 5.2 0 7.2M7 3.4c1.6 2 1.6 5.2 0 7.2" fill="none" stroke="#fff" stroke-width="0.7"/></svg>
          <span>www.cedarlinevinyl.com</span>
        </li>
      </ul>
    </div>
  </section>

</body>
</html>
```